Honey Bottle Labels for Honey Business

The honey is a niche product and the logo should exude a strong impression of wild and raw honey and natural – as in natural beekeeping. We try to keep things as simple as possible; this includes the processes the honey goes through.
We are looking for something with a gourmet / classy upmarket look and feel design. For example: Ideas with bees, honeycomb, modern or hexagonal feature; something eye catching, but not too busy.
Our honey is all natural and organic. We are a clean, simple yet sophisticated business, so would like our logo to reflect these principles.

Feel free to expand your creativity to anything you may think would look awesome and original!

The label needs to contain:
1. Our company logo. (Please see attached)
2. 100% Pure Raw Honey / Local
3. Net Wt: 16 oz (454 g) (this is the weight of the honey and will need to be modified based on bottle size.)
4. Address, Pine Hollow, MN 56000 (not larger than 1/16th inch)

Needs to be versatile to include possibility of clear label, I have included some example pictures as ideas (oval, round, square tags)

Sizes needed:
Large oval 2 5/8" x 4 1/2"
Small oval: 1 3/4" wide x 3" tall
Rectangle 1 3/4" tall x 5" wide
Round diameter 2.5"

Target Market(s)

Gourmet stores, market stall, local tourist market, potential store door sales

Requirements
Must have
• - A design that can be used on various packaging, jars and containers. We are hoping to scale up the production and want something to suit.
• - has to have a wow to stand out on the supermarket shelves
Nice to have
• Things we like:
• Minimalist designs
• Clever designs
• We don't like hand drawn font types
• We are open to the use of a hexagon in the logo, but not must have
Should not have
• Things we do not like:
• Too many colors

```html
<!DOCTYPE html>
<html lang="en">
<head>
<meta charset="utf-8">
<title>Meadow Ridge Honey – Label Options</title>
<link href="https://fonts.googleapis.com/css2?family=Oswald:wght@500;600&family=Quicksand:wght@600&family=Roboto:wght@400&display=swap" rel="stylesheet">
<style>
  :root{
    --page:#f3f3f1;
    --band:#ebebe8;
    --label-white:#ffffff;
    --label-cream:#f1ead3;
    --label-black:#141414;
    --honey:#f5a623;
    --amber:#ea6a1c;
    --rust:#d2431b;
    --ink:#1d1d1d;
    --grey:#b9b9b9;
    --caption:#111111;
  }
  html,body{margin:0;padding:0;}
  body{
    width:1200px;height:2299px;overflow:hidden;
    background:var(--page);
    position:relative;
    font-family:"Oswald",sans-serif;
  }
  .option-set{position:absolute;left:0;width:1200px;}
  .set-wrap{top:0;height:697px;}
  .set-oval{top:697px;height:905px;background:var(--band);}
  .set-round{top:1602px;height:697px;}

  .brand-mark{
    position:absolute;left:50%;transform:translateX(-50%);
    display:flex;align-items:center;gap:8px;
    font-family:"Quicksand",sans-serif;font-weight:600;
    color:var(--honey);white-space:nowrap;
  }
  .brand-mark .dot{display:inline-block;width:14px;height:14px;border-radius:50%;background:var(--honey);}
  .set-wrap .brand-mark{top:52px;font-size:30px;}
  .set-oval .brand-mark{top:88px;font-size:36px;}
  .set-round .brand-mark{top:72px;font-size:30px;}

  .label{position:absolute;display:block;}
  .caption{
    position:absolute;width:240px;text-align:center;
    font-family:"Roboto",sans-serif;font-size:24px;color:var(--caption);
  }
  svg text{font-family:"Oswald",sans-serif;}
  svg .name{font-family:"Quicksand",sans-serif;font-weight:600;}
</style>
</head>
<body>

<!-- Wrap-around labels -->
<section class="option-set set-wrap">
  <div class="brand-mark"><span class="dot"></span>meadow ridge honey</div>

  <svg class="label" style="left:61px;top:238px" width="340" height="350" viewBox="0 0 340 350">
    <defs><path id="w1arc" d="M 62 175 A 108 108 0 0 1 278 175"/></defs>
    <rect width="340" height="350" fill="var(--label-white)"/>
    <line x1="0" y1="210" x2="50" y2="210" stroke="var(--grey)" stroke-width="2"/>
    <line x1="290" y1="210" x2="340" y2="210" stroke="var(--grey)" stroke-width="2"/>
    <text font-size="30" font-weight="600" fill="var(--ink)" text-anchor="middle"><textPath href="#w1arc" startOffset="50%">100% PURE RAW HONEY</textPath></text>
    <circle cx="170" cy="190" r="88" fill="none" stroke="var(--amber)" stroke-width="3"/>
    <text class="name" x="170" y="200" font-size="26" fill="var(--amber)" text-anchor="middle">meadow ridge</text>
    <text class="name" x="170" y="230" font-size="26" fill="var(--amber)" text-anchor="middle">honey</text>
    <text x="170" y="305" font-size="15" font-weight="500" fill="var(--ink)" text-anchor="middle">NET WT: 16 OZ (454 G)</text>
    <text x="170" y="333" font-size="20" font-weight="600" fill="var(--rust)" text-anchor="middle" letter-spacing="1">PINE HOLLOW, MN 56000</text>
  </svg>
  <div class="caption" style="left:111px;top:650px">Option 1</div>

  <svg class="label" style="left:430px;top:238px" width="340" height="350" viewBox="0 0 340 350">
    <defs><path id="w2arc" d="M 62 175 A 108 108 0 0 1 278 175"/></defs>
    <rect width="340" height="350" fill="var(--label-cream)"/>
    <text font-size="30" font-weight="600" fill="var(--ink)" text-anchor="middle"><textPath href="#w2arc" startOffset="50%">100% PURE RAW HONEY</textPath></text>
    <circle cx="170" cy="190" r="88" fill="none" stroke="var(--amber)" stroke-width="3"/>
    <text class="name" x="170" y="200" font-size="26" fill="var(--amber)" text-anchor="middle">meadow ridge</text>
    <text class="name" x="170" y="230" font-size="26" fill="var(--amber)" text-anchor="middle">honey</text>
    <text x="170" y="305" font-size="15" font-weight="500" fill="var(--ink)" text-anchor="middle">NET WT: 16 OZ (454 G)</text>
    <text x="170" y="333" font-size="20" font-weight="600" fill="var(--rust)" text-anchor="middle" letter-spacing="1">PINE HOLLOW, MN 56000</text>
  </svg>
  <div class="caption" style="left:480px;top:650px">Option 2</div>

  <svg class="label" style="left:800px;top:238px" width="340" height="350" viewBox="0 0 340 350">
    <defs><path id="w3arc" d="M 62 175 A 108 108 0 0 1 278 175"/></defs>
    <rect width="340" height="350" fill="var(--label-black)"/>
    <text font-size="30" font-weight="600" fill="var(--amber)" text-anchor="middle"><textPath href="#w3arc" startOffset="50%">100% PURE RAW HONEY</textPath></text>
    <circle cx="170" cy="190" r="88" fill="none" stroke="var(--honey)" stroke-width="3"/>
    <text class="name" x="170" y="200" font-size="26" fill="var(--honey)" text-anchor="middle">meadow ridge</text>
    <text class="name" x="170" y="230" font-size="26" fill="var(--honey)" text-anchor="middle">honey</text>
    <text x="170" y="305" font-size="15" font-weight="500" fill="#ffffff" text-anchor="middle">NET WT: 16 OZ (454 G)</text>
    <text x="170" y="333" font-size="20" font-weight="600" fill="var(--amber)" text-anchor="middle" letter-spacing="1">PINE HOLLOW, MN 56000</text>
  </svg>
  <div class="caption" style="left:850px;top:650px">Option 3</div>
</section>

<!-- Oval labels -->
<section class="option-set set-oval">
  <div class="brand-mark"><span class="dot"></span>meadow ridge honey</div>

  <svg class="label" style="left:115px;top:323px" width="230" height="460" viewBox="0 0 230 460">
    <ellipse cx="115" cy="230" rx="113" ry="228" fill="var(--label-white)"/>
    <ellipse cx="115" cy="230" rx="103" ry="217" fill="none" stroke="var(--honey)" stroke-width="3"/>
    <text class="name" x="115" y="140" font-size="24" fill="var(--amber)" text-anchor="middle">meadow ridge</text>
    <text class="name" x="115" y="166" font-size="24" fill="var(--amber)" text-anchor="middle">honey</text>
    <text x="115" y="250" font-size="36" font-weight="600" fill="var(--ink)" text-anchor="middle">100% PURE</text>
    <text x="115" y="292" font-size="36" font-weight="600" fill="var(--amber)" text-anchor="middle">RAW HONEY</text>
    <line x1="45" y1="306" x2="185" y2="306" stroke="var(--honey)" stroke-width="1.5"/>
    <text x="115" y="324" font-size="11" font-weight="500" fill="var(--ink)" text-anchor="middle">NET WT: 16 OZ (454 G)</text>
    <text x="115" y="342" font-size="13" font-weight="600" fill="var(--rust)" text-anchor="middle">PINE HOLLOW, MN 56000</text>
    <circle cx="62" cy="370" r="13" fill="var(--ink)"/>
  </svg>
  <div class="caption" style="left:110px;top:855px">Option 1</div>

  <svg class="label" style="left:486px;top:323px" width="230" height="460" viewBox="0 0 230 460">
    <ellipse cx="115" cy="230" rx="113" ry="228" fill="var(--label-cream)"/>
    <ellipse cx="115" cy="230" rx="103" ry="217" fill="none" stroke="var(--honey)" stroke-width="3"/>
    <text class="name" x="115" y="140" font-size="24" fill="var(--amber)" text-anchor="middle">meadow ridge</text>
    <text class="name" x="115" y="166" font-size="24" fill="var(--amber)" text-anchor="middle">honey</text>
    <text x="115" y="250" font-size="36" font-weight="600" fill="var(--ink)" text-anchor="middle">100% PURE</text>
    <text x="115" y="292" font-size="36" font-weight="600" fill="var(--amber)" text-anchor="middle">RAW HONEY</text>
    <line x1="45" y1="306" x2="185" y2="306" stroke="var(--honey)" stroke-width="1.5"/>
    <text x="115" y="324" font-size="11" font-weight="500" fill="var(--ink)" text-anchor="middle">NET WT: 16 OZ (454 G)</text>
    <text x="115" y="342" font-size="13" font-weight="600" fill="var(--rust)" text-anchor="middle">PINE HOLLOW, MN 56000</text>
    <circle cx="62" cy="370" r="13" fill="var(--ink)"/>
  </svg>
  <div class="caption" style="left:481px;top:855px">Option 2</div>

  <svg class="label" style="left:862px;top:323px" width="230" height="460" viewBox="0 0 230 460">
    <ellipse cx="115" cy="230" rx="113" ry="228" fill="var(--label-black)"/>
    <ellipse cx="115" cy="230" rx="103" ry="217" fill="none" stroke="var(--honey)" stroke-width="3"/>
    <text class="name" x="115" y="140" font-size="24" fill="var(--honey)" text-anchor="middle">meadow ridge</text>
    <text class="name" x="115" y="166" font-size="24" fill="var(--honey)" text-anchor="middle">honey</text>
    <text x="115" y="250" font-size="36" font-weight="600" fill="#cfcfcf" text-anchor="middle">100% PURE</text>
    <text x="115" y="292" font-size="36" font-weight="600" fill="var(--amber)" text-anchor="middle">RAW HONEY</text>
    <line x1="45" y1="306" x2="185" y2="306" stroke="var(--honey)" stroke-width="1.5"/>
    <text x="115" y="324" font-size="11" font-weight="500" fill="#ffffff" text-anchor="middle">NET WT: 16 OZ (454 G)</text>
    <text x="115" y="342" font-size="13" font-weight="600" fill="var(--amber)" text-anchor="middle">PINE HOLLOW, MN 56000</text>
    <circle cx="62" cy="370" r="13" fill="var(--honey)"/>
  </svg>
  <div class="caption" style="left:857px;top:855px">Option 3</div>
</section>

<!-- Round labels -->
<section class="option-set set-round">
  <div class="brand-mark"><span class="dot"></span>meadow ridge honey</div>

  <svg class="label" style="left:92px;top:297px" width="310" height="310" viewBox="0 0 310 310">
    <defs>
      <path id="r1top" d="M 42 155 A 113 113 0 0 1 268 155"/>
      <path id="r1bot" d="M 30 165 A 125 125 0 0 0 280 165"/>
    </defs>
    <circle cx="155" cy="155" r="153" fill="var(--label-white)"/>
    <circle cx="155" cy="155" r="143" fill="none" stroke="var(--honey)" stroke-width="3" stroke-dasharray="2 4"/>
    <text font-size="30" font-weight="600" fill="var(--ink)" text-anchor="middle"><textPath href="#r1top" startOffset="50%">100% PURE RAW HONEY</textPath></text>
    <circle cx="155" cy="160" r="80" fill="none" stroke="var(--honey)" stroke-width="3"/>
    <circle cx="155" cy="120" r="11" fill="var(--ink)"/>
    <text class="name" x="155" y="166" font-size="23" fill="var(--amber)" text-anchor="middle">meadow ridge</text>
    <text class="name" x="155" y="193" font-size="23" fill="var(--amber)" text-anchor="middle">honey</text>
    <text x="155" y="216" font-size="11" font-weight="500" fill="var(--ink)" text-anchor="middle">NET WT: 16 OZ (454 G)</text>
    <text font-size="17" font-weight="600" fill="var(--rust)" text-anchor="middle" letter-spacing="1"><textPath href="#r1bot" startOffset="50%">PINE HOLLOW, MN 56000</textPath></text>
  </svg>
  <div class="caption" style="left:127px;top:655px">Option 1</div>

  <svg class="label" style="left:446px;top:297px" width="310" height="310" viewBox="0 0 310 310">
    <defs>
      <path id="r2top" d="M 42 155 A 113 113 0 0 1 268 155"/>
      <path id="r2bot" d="M 30 165 A 125 125 0 0 0 280 165"/>
    </defs>
    <circle cx="155" cy="155" r="153" fill="var(--label-cream)"/>
    <circle cx="155" cy="155" r="143" fill="none" stroke="var(--honey)" stroke-width="3" stroke-dasharray="2 4"/>
    <text font-size="30" font-weight="600" fill="var(--ink)" text-anchor="middle"><textPath href="#r2top" startOffset="50%">100% PURE RAW HONEY</textPath></text>
    <circle cx="155" cy="160" r="80" fill="none" stroke="var(--honey)" stroke-width="3"/>
    <circle cx="155" cy="120" r="11" fill="var(--ink)"/>
    <text class="name" x="155" y="166" font-size="23" fill="var(--amber)" text-anchor="middle">meadow ridge</text>
    <text class="name" x="155" y="193" font-size="23" fill="var(--amber)" text-anchor="middle">honey</text>
    <text x="155" y="216" font-size="11" font-weight="500" fill="var(--ink)" text-anchor="middle">NET WT: 16 OZ (454 G)</text>
    <text font-size="17" font-weight="600" fill="var(--rust)" text-anchor="middle" letter-spacing="1"><textPath href="#r2bot" startOffset="50%">PINE HOLLOW, MN 56000</textPath></text>
  </svg>
  <div class="caption" style="left:481px;top:655px">Option 2</div>

  <svg class="label" style="left:811px;top:297px" width="310" height="310" viewBox="0 0 310 310">
    <defs>
      <path id="r3top" d="M 42 155 A 113 113 0 0 1 268 155"/>
      <path id="r3bot" d="M 30 165 A 125 125 0 0 0 280 165"/>
    </defs>
    <circle cx="155" cy="155" r="153" fill="var(--label-black)"/>
    <circle cx="155" cy="155" r="143" fill="none" stroke="var(--honey)" stroke-width="3" stroke-dasharray="2 4"/>
    <text font-size="30" font-weight="600" fill="#d8d8d8" text-anchor="middle"><textPath href="#r3top" startOffset="50%">100% PURE RAW HONEY</textPath></text>
    <circle cx="155" cy="160" r="80" fill="none" stroke="var(--honey)" stroke-width="3"/>
    <circle cx="155" cy="120" r="11" fill="var(--honey)"/>
    <text class="name" x="155" y="166" font-size="23" fill="var(--honey)" text-anchor="middle">meadow ridge</text>
    <text class="name" x="155" y="193" font-size="23" fill="var(--honey)" text-anchor="middle">honey</text>
    <text x="155" y="216" font-size="11" font-weight="500" fill="#ffffff" text-anchor="middle">NET WT: 16 OZ (454 G)</text>
    <text font-size="17" font-weight="600" fill="var(--amber)" text-anchor="middle" letter-spacing="1"><textPath href="#r3bot" startOffset="50%">PINE HOLLOW, MN 56000</textPath></text>
  </svg>
  <div class="caption" style="left:846px;top:655px">Option 3</div>
</section>

</body>
</html>
```